We are looking for a logo AND business card design.  We are a sponsor who provides an international experience for individuals both in the U.S. and abroad to improve work skills, gain life experiences, and language skills while making the world a better, more understood place to live. 

Business card:  Lorna Pickett

Bright Horizon Passage, 5427 Amber Hollow Lane, Marlow Springs, GA 30412  (770) 481-3027   www.brighthorizonpassage.example

Logo does not have to be literal.  A good graphic with words would be acceptable also.

Logo Text

Requirements
Must have
• Please embed fonts in the vector file so we and our printers can add / change names as we grow AND AI file.
Nice to have
• Open to font and color but must be professional.  Name does not need to be in logo.
Should not have
• Pastels or flourescents.

```html
<!DOCTYPE html>
<html lang="en">
<head>
<meta charset="utf-8">
<title>Lorna Pickett – Bright Horizon Passage</title>
<link href="https://fonts.googleapis.com/css2?family=Poppins:wght@800&family=Questrial&display=swap" rel="stylesheet">
<style>
  :root {
    --navy: #0f3471;
    --white: #ffffff;
    --ring-grey: #d3d5d8;
    --ink: #1c1c1c;
  }
  html, body {
    margin: 0;
    padding: 0;
    overflow: hidden;
    background: var(--white);
  }
  .card {
    position: relative;
    width: 1200px;
    height: 686px;
    background: var(--white);
    overflow: hidden;
  }
  .card__band {
    position: absolute;
    left: 0;
    top: 0;
  }
  .identity {
    position: absolute;
    left: 115px;
    top: 170px;
    color: var(--white);
  }
  .identity__name {
    margin: 0;
    font-family: "Poppins", sans-serif;
    font-weight: 800;
    font-size: 32px;
    letter-spacing: 1.5px;
    line-height: 1;
    text-transform: uppercase;
  }
  .identity__company {
    margin: 14px 0 0;
    font-family: "Questrial", sans-serif;
    font-size: 32px;
    line-height: 1;
  }
  .brand-mark {
    position: absolute;
    left: 906px;
    top: 114px;
    width: 212px;
    height: 212px;
    display: flex;
    align-items: center;
    justify-content: center;
    text-align: center;
    font-family: "Questrial", sans-serif;
    font-size: 26px;
    line-height: 1.2;
    color: var(--white);
  }
  .contact {
    position: absolute;
    right: 94px;
    top: 418px;
    margin: 0;
    font-family: "Questrial", sans-serif;
    font-style: normal;
    font-size: 29px;
    line-height: 44px;
    text-align: right;
    color: var(--ink);
  }
  .contact span { display: block; }
</style>
</head>
<body>
  <div class="card">
    <svg class="card__band" width="1200" height="686" viewBox="0 0 1200 686" aria-hidden="true">
      <rect x="0" y="96" width="1005" height="253" fill="var(--navy)"/>
      <circle cx="1000" cy="220" r="134" fill="var(--ring-grey)"/>
      <circle cx="1012" cy="220" r="130" fill="var(--white)"/>
      <circle cx="1012" cy="220" r="106" fill="var(--navy)"/>
    </svg>

    <div class="brand-mark">Bright<br>Horizon<br>Passage</div>

    <div class="identity">
      <h1 class="identity__name">Lorna Pickett</h1>
      <p class="identity__company">Bright Horizon Passage</p>
    </div>

    <address class="contact">
      <span class="contact__street">5427 Amber Hollow Lane</span>
      <span class="contact__city">Marlow Springs, GA 30412</span>
      <span class="contact__phone">(555) 481-3027</span>
      <span class="contact__web">www.brighthorizonpassage.example</span>
    </address>
  </div>
</body>
</html>
```